Do me a Simple layout and Blow the stockings off my clients!!

I am a Personal Stylist focusing on helping women/mothers needing to revamp their wardrobe and feel confident and fresh again. I'm receiving very positive feedback and growing interest in the services I offer. I provide a 'Client Profile' as part of that service in a word document (saved as PDF). What I'm needing is to turn the average looking word document into a modern, funky and professional document template. I have a business logo and copy.
The template should be fluid, easy to update and communicate sassy, funky and professional.

Target Market(s)

Females 25-65.

Industry/Entity Type

Business

Font styles to use
Other font styles liked:
• HelveticaNeue Condensed, or Raleway

Requirements
Must have
• Colours and styles consistent with logo, and fashion industry.
• Interesting and emotive elements around the content.
• Create clear 'sections' with high impact (full coloured page with single, simple section heading ?)
Nice to have
• Ability to feature 'subjects' photos in interesting ways through out the document.
• Don't just stick with portrait layout, landscape is fine too.
Should not have
• Not too busy - less is more.

```html
<!DOCTYPE html>
<html lang="en">
<head>
<meta charset="utf-8">
<title>Client Profile – Lara Whitfield Personal Shopping</title>
<link rel="stylesheet" href="https://fonts.googleapis.com/css2?family=Oswald:wght@500&family=Raleway:wght@400;500&family=Cormorant+Garamond:ital,wght@0,500;1,400&display=swap">
<style>
  :root {
    --pink: #e2288f;
    --pink-soft: #f3b8d6;
    --violet: #b46ad8;
    --sky: #9fd4ef;
    --blush: #f7d3d8;
    --ink: #2b2b2b;
    --grey: #8d8d8d;
    --page-edge: #e6e6e6;
    --paper: #ffffff;
  }
  * { box-sizing: border-box; margin: 0; padding: 0; }
  html, body { width: 1200px; height: 628px; overflow: hidden; background: var(--paper); }
  body { position: relative; font-family: "Raleway", sans-serif; color: var(--ink); }

  .page {
    position: absolute;
    background: var(--paper);
    border: 1px solid var(--page-edge);
    overflow: hidden;
  }
  .page--cover { left: 25px; top: 12px; width: 305px; height: 493px; }
  .page--analysis { left: 390px; top: 100px; width: 400px; height: 478px; }
  .page--notes { left: 782px; top: 16px; width: 393px; height: 584px; z-index: 2; }

  .brand {
    position: absolute;
    color: var(--pink);
    font-family: "Raleway", sans-serif;
    font-weight: 500;
    font-size: 13px;
    line-height: 1;
    letter-spacing: .02em;
    white-space: nowrap;
  }

  /* Cover */
  .page--cover .brand { right: 16px; top: 20px; }
  .cover__artwork {
    position: absolute; left: 20px; top: 60px; width: 270px; height: 290px;
    background:
      radial-gradient(ellipse 45% 40% at 30% 55%, rgba(159,212,239,.85), transparent 70%),
      radial-gradient(ellipse 50% 45% at 70% 50%, rgba(226,40,143,.55), transparent 72%),
      radial-gradient(ellipse 60% 55% at 50% 45%, rgba(180,106,216,.55), transparent 75%);
  }
  .cover__title {
    position: absolute; left: 0; right: 0; top: 228px; text-align: center;
    font-family: "Oswald", sans-serif; font-weight: 500; color: var(--pink);
  }
  .cover__title-main { display: block; font-size: 78px; line-height: 1; letter-spacing: .01em; }
  .cover__title-sub { display: block; font-size: 26px; line-height: 1; margin-top: 4px; padding-left: 40px; }
  .cover__owner { position: absolute; left: 20px; top: 441px; font-size: 15px; line-height: 1.35; }
  .cover__owner-name { display: block; color: var(--ink); }
  .cover__owner-service { display: block; color: var(--pink); }

  /* Shared decoration */
  .splash {
    position: absolute;
    background:
      radial-gradient(ellipse 40% 30% at 40% 20%, rgba(247,211,216,.9), transparent 70%),
      radial-gradient(ellipse 45% 30% at 55% 55%, rgba(243,184,214,.6), transparent 70%),
      radial-gradient(ellipse 50% 30% at 45% 88%, rgba(159,212,239,.55), transparent 70%);
  }
  .figure-art {
    position: absolute;
    background: linear-gradient(180deg, rgba(226,40,143,.55), rgba(180,106,216,.55));
    border-radius: 40% 40% 10% 10% / 20% 20% 5% 5%;
    opacity: .8;
  }

  /* Analysis page */
  .page--analysis .splash { left: 0; top: 0; width: 400px; height: 478px; }
  .page--analysis .figure-art { left: 22px; top: 308px; width: 80px; height: 165px; }
  .analysis__body { position: absolute; left: 150px; top: 48px; width: 240px; font-size: 7.4px; line-height: 1.38; }
  .heading { font-family: "Cormorant Garamond", serif; color: var(--ink); line-height: .9; }
  .heading__lead { display: block; font-size: 21px; font-weight: 500; }
  .heading__accent { display: block; font-style: italic; color: var(--grey); font-size: 28px; letter-spacing: .04em; }
  .analysis__body .heading { margin-bottom: 12px; }
  .analysis__body .heading__accent { padding-left: 70px; }
  .field { margin-bottom: 9px; }
  .label { color: var(--pink); font-weight: 500; font-size: 8.2px; }
  .ticks { list-style: none; padding-left: 4px; }
  .ticks li { position: relative; padding-left: 8px; }
  .ticks li::before { content: "✔"; position: absolute; left: 0; font-size: 6px; top: 1px; }
  .page--analysis .brand { left: 262px; top: 440px; }

  /* Notes page */
  .page--notes .splash { left: 0; top: 0; width: 200px; height: 584px; }
  .page--notes .figure-art { left: 22px; top: 350px; width: 82px; height: 178px; }
  .notes__heading { position: absolute; left: 140px; top: 10px; text-align: center; width: 245px; }
  .notes__heading .heading__lead { font-size: 22px; }
  .notes__heading .heading__accent { font-size: 24px; padding-left: 25px; }
  .notes__photo {
    position: absolute; left: 124px; width: 68px; height: 106px;
    background: linear-gradient(160deg, #d9cfc4, #6f6460 55%, #3b3434);
  }
  .notes__photo--first { top: 100px; }
  .notes__photo--second { top: 232px; background: linear-gradient(160deg, #e2ddd5, #b8aea3 45%, #2f2c2c); }
  .notes__text { position: absolute; left: 208px; top: 104px; width: 178px; font-size: 7.1px; line-height: 1.42; }
  .notes__text p + p { margin-top: 9px; }
  .page--notes .brand { right: 16px; top: 536px; }
</style>
</head>
<body>

<section class="page page--cover">
  <p class="brand">Wardrobe Bloom</p>
  <div class="cover__artwork" role="img" aria-label="Glowing pink and blue fashion illustration of three women silhouettes with stars"></div>
  <h1 class="cover__title"><span class="cover__title-main">CLIENT</span><span class="cover__title-sub">PROFILE</span></h1>
  <p class="cover__owner"><span class="cover__owner-name">LARA WHITFIELD</span><span class="cover__owner-service">PERSONAL SHOPPING</span></p>
</section>

<section class="page page--analysis">
  <div class="splash" role="img" aria-label="Soft pink and blue watercolour splash"></div>
  <div class="figure-art" role="img" aria-label="Pink silhouette illustration of a woman in a hat"></div>
  <div class="analysis__body">
    <h2 class="heading"><span class="heading__lead">Style Analysis</span><span class="heading__accent">REPORT</span></h2>
    <p class="field"><span class="label">Client:</span> Jess</p>
    <p class="field"><span class="label">Body Shape:</span> The Brick, shorter waist.</p>
    <div class="field"><p class="label">Main characteristics:</p>
      <ul class="ticks"><li>Broad shoulders</li><li>Hips inline with shoulders</li><li>No shapely waist line</li><li>Possibly larger (ish) thighs</li></ul></div>
    <div class="field"><p class="label">Main goals in dressing ‘The Brick’:</p>
      <ul class="ticks"><li>Create curves using shapely, flowing pieces</li><li>Look for curved edges on garments</li><li>Sweetheart necklines will instantly create a more shapely start to your upper body</li><li>Use patterns to accentuate your best areas and detract from others.</li><li>Use stripes of varying sizes, to create a shapely illusion</li><li>For accessories look for curvy jewelry and handbags</li></ul></div>
    <div class="field"><p class="label">STYLES TO AVOID:</p>
      <ul class="ticks"><li>Square cut or boxed edge jackets</li><li>Short skirts (mini) or shorts which will cut you off mid thigh</li><li>Box pleats or pleats at the front of trousers</li><li>Look for shoes that add to the flow of your garment, nothing too solid, or chunky</li></ul></div>
    <p class="field"><span class="label">Celebrity ‘Bricks’:</span> Mara Ellison, Nina Prescott, Carla Dunmore</p>
  </div>
  <p class="brand">Wardrobe Bloom</p>
</section>

<section class="page page--notes">
  <div class="splash" role="img" aria-label="Soft pink and blue watercolour splash"></div>
  <div class="figure-art" role="img" aria-label="Pink silhouette illustration of a woman in a hat"></div>
  <h2 class="heading notes__heading"><span class="heading__lead">Notes from your</span><span class="heading__accent">STYLING session</span></h2>
  <div class="notes__photo notes__photo--first" role="img" aria-label="Client photo in fitting room wearing black lace dress"></div>
  <div class="notes__photo notes__photo--second" role="img" aria-label="Client photo in fitting room wearing white top and black palazzo trousers"></div>
  <div class="notes__text">
    <p>This really is a beautiful dress. The black lace section is the main part of the dress that catches your eye, making your waist look longer and giving you a curvier silhouette. The round neckline works in this instance, thanks to the black V-section across the bust giving that illusion of a longer décolletage, which is what you want to create. This length is perfect; it makes your legs look fantastic. Pair this with some great black heels, your hair up and introduce a coloured clutch, would look amazing.</p>
    <p>Ok, so these palazzo trousers were terrible and we realised that the pleats are a no go! The fabric is great for you; the softer more ‘flowy’ material gives you a shapelier look. The colour and the pattern (small, fine, beige spot) look great on you and very sophisticated. The top is a great colour of white; I think it looks more ‘vintage’ white, instead of famous ‘Hollywood star teeth’ white, giving you a more polished look. The cuffed sleeve works really well for your arm section, giving a bit of something different to what could be a plain white top. If it didn’t have that layered section in the middle I think it would work even better, as this cuts you off mid section and it does so in-line with your elbows, creating a boxy look to your torso. Not the look you’re trying to achieve! If it had been all one length it would be a great top.</p>
  </div>
  <p class="brand">Wardrobe Bloom</p>
</section>

</body>
</html>
```